One of Australia's fastest growing Financial Company looking for an updated business card design!

Meridale Partners Australia is looking for an updated design for our business cards. We would like to keep up our professional appearances and have get new exciting design that fits our company.

The Meridale aim is to facilitate and assist clients in every financial requirement that may arise in financial areas.

We would to see the design to use colour blue and we like the clouds in the background. We have attached two designs we have use before but we need something with more professional and easy to read design.

We would like the website in the back of the card; the employees name more central and stands out; only a postal address; a list of all our locations along the bottom (Sydney, Melbourne, Brisbane, Singapore)

Looking forward to seeing the designs come in!

Target Market(s)

Other Industry Professionals
Middle Class Families

Industry/Entity Type

Finance

Contact Information for Business Card

Name; Company Role; Office Number; Mobile Number; Email Address; Website; Postal Address; Locations

Font styles to use
Serif
Sans Serif

Colors
0492cd
33a6d7
85cae6
85acd3
3176b5
0455a3
cee9f5
d5e2ee

Requirements
Must have
• Name; Company Role; Office Number; Mobile Number; Email Address; Website; Postal Address; Locations
Nice to have
• The colour blue, clouds on the background

```html
<!DOCTYPE html>
<html lang="en">
<head>
<meta charset="utf-8">
<title>Meridale Partners Australia – Business Card</title>
<link rel="stylesheet" href="https://fonts.googleapis.com/css2?family=Arimo:wght@400;700&display=swap">
<style>
  :root {
    --bg: #e9ecef;
    --blue-light: #33a6d7;
    --blue-mid: #0492cd;
    --blue-deep: #0455a3;
    --red: #e8403d;
    --white: #ffffff;
    --brand-blue: #1f8fd6;
  }
  * { box-sizing: border-box; margin: 0; padding: 0; }
  html, body {
    width: 1200px; height: 950px; overflow: hidden;
    background: var(--bg);
    font-family: "Arimo", Arial, sans-serif;
  }
  .sheet {
    position: relative; width: 1200px; height: 950px;
    display: flex; flex-direction: column; align-items: center;
    justify-content: center; gap: 40px;
  }
  .card {
    position: relative; width: 680px; height: 415px; overflow: hidden;
    box-shadow: 0 6px 18px rgba(0,0,0,.18);
  }

  /* Front */
  .card-front {
    background: radial-gradient(ellipse at 40% 35%, var(--blue-light) 0%, var(--blue-mid) 55%, #0a6cb8 100%);
    color: var(--white);
  }
  .front-brand {
    position: absolute; left: 0; right: 0; top: 148px;
    display: flex; align-items: center; justify-content: center; gap: 16px;
  }
  .brand-dot {
    width: 30px; height: 30px; border-radius: 50%; background: var(--white);
  }
  .front-brand .brand-name {
    font-size: 72px; font-weight: 700; letter-spacing: -1px; color: var(--white);
  }
  .locations {
    position: absolute; left: 0; right: 0; top: 262px;
    text-align: center; font-size: 18px; letter-spacing: .5px;
  }
  .locations .sep { margin: 0 10px; }

  /* Back */
  .card-back { background: var(--white); }
  .back-panel { position: absolute; inset: 0; width: 680px; height: 415px; }
  .back-panel path { fill: var(--red); }
  .details {
    position: absolute; left: 34px; top: 30px; color: var(--white);
  }
  .person-name { font-size: 27px; font-weight: 700; }
  .person-role { font-size: 18px; font-weight: 700; margin-top: 4px; }
  .address { font-size: 16px; line-height: 1.35; margin-top: 26px; }
  .contact-list { list-style: none; font-size: 16px; line-height: 1.35; margin-top: 2px; }
  .contact-list li { display: flex; align-items: center; gap: 8px; }
  .contact-list svg { width: 14px; height: 14px; fill: var(--white); flex: none; }
  .contact-list .plain { padding-left: 0; }
  .back-brand {
    position: absolute; right: 34px; bottom: 34px;
    display: flex; align-items: center; gap: 10px;
  }
  .back-brand .brand-dot { width: 20px; height: 20px; background: var(--red); }
  .back-brand .brand-name {
    font-size: 44px; font-weight: 700; letter-spacing: -1px; color: var(--brand-blue);
  }
</style>
</head>
<body>
<main class="sheet">
  <section class="card card-front" aria-label="Card front">
    <div class="front-brand">
      <span class="brand-dot"></span>
      <span class="brand-name">Meridale</span>
    </div>
    <p class="locations">Sydney<span class="sep">•</span>Melbourne<span class="sep">•</span>Brisbane<span class="sep">•</span>Singapore</p>
  </section>

  <section class="card card-back" aria-label="Card back">
    <svg class="back-panel" viewBox="0 0 680 415" aria-hidden="true">
      <path d="M0 0 H390 C470 110 360 290 440 415 H0 Z"/>
    </svg>
    <div class="details">
      <h1 class="person-name">Claire Hollis</h1>
      <p class="person-role">Investment Consultant</p>
      <p class="address">42 Harbour Lane<br>Port Aldwyn, NSW 2400</p>
      <ul class="contact-list">
        <li><svg viewBox="0 0 24 24" aria-hidden="true"><path d="M6.6 10.8a15 15 0 0 0 6.6 6.6l2.2-2.2a1 1 0 0 1 1-.25 11.4 11.4 0 0 0 3.6.57 1 1 0 0 1 1 1V20a1 1 0 0 1-1 1A17 17 0 0 1 3 4a1 1 0 0 1 1-1h3.5a1 1 0 0 1 1 1c0 1.25.2 2.46.57 3.6a1 1 0 0 1-.25 1z"/></svg>(02) 5550 1834</li>
        <li><svg viewBox="0 0 24 24" aria-hidden="true"><path d="M7 1h10a2 2 0 0 1 2 2v18a2 2 0 0 1-2 2H7a2 2 0 0 1-2-2V3a2 2 0 0 1 2-2zm0 3v14h10V4zm5 15.5a1.2 1.2 0 1 0 0 2.4 1.2 1.2 0 0 0 0-2.4z"/></svg>0400 555 218</li>
        <li class="plain">info@meridalepartners.com.au</li>
        <li class="plain">www.meridalepartners.com.au</li>
      </ul>
    </div>
    <div class="back-brand">
      <span class="brand-dot"></span>
      <span class="brand-name">Meridale</span>
    </div>
  </section>
</main>
</body>
</html>
```